Office Wall Poster plus other Wall Decal quotes in office

We have redesigned our office & require parts of our Culture statement to be displayed in our office. Our company is KOVA Estate Agents Group and our brand is all about being KOVA .. integrity, honesty, authenticity etc.
We have two areas we wish to decorate.
1. Reception
2. Meeting Room

RECEPTION
We want our leading culture statement to be displayed as large A0 size in a framed POSTER PRINT in our reception. The frame will be black.
WORDING: 'There's a reason we're called KOVA. KOVA is the essence of who we are'
Our brand colors are red, white, black. Our Red is CMYK 12,99, 92,02
When we type our name KOVA, we always use Venera font (always in caps). I have attached a file I personally created with 3 different ideas (I am not a designer) but we are not happy with any of them but it will give you an idea of what we are looking for. We want a simple statement so it stands out and not too busy.

MEETING ROOM
We have one black feature wall in this room and wish to dress this with a collection of quotes from our main Culture statement. We will have these printed as 'stick on wall decals' We have provided a collection of 8 quotes for you to design. Wording is to be in white colour with the key words to be METALLIC SILVER & in caps. We were planning to arrange them ad-hoc on the wall singularly, but if you have any creative ideas on how to display these, we are open to suggestions. Please provide your ideas on how best to arrange these on the black wall. Maybe even in a circle to represent our logo? But we truly do not have a clue - we are only real estate agents, not designers. That is why we would love suggetions on how best to make our Culture Statements work best.
Best of luck and we are excited to see your ideas!

Target Market(s)

Our clients need to get a great feel for what we are all about when they visit our office. Our culture needs to be seen and felt.

Industry/Entity Type

Real Estate

Font styles to use
Other font styles liked:
• We use Venera font when we type our name KOVA

Colors
EB3D1F
EC4F4E
F09395
F8D3D4
FCEDEE

Requirements
Should not have
• Not too busy, simple statements, easy to read

```html
<!DOCTYPE html>
<html lang="en">
<head>
<meta charset="utf-8">
<title>KOVA Culture Poster</title>
<link rel="stylesheet" href="https://fonts.googleapis.com/css2?family=Bebas+Neue&family=Michroma&display=swap">
<style>
  :root {
    --backdrop: #dcdcdc;
    --blush: #f8d3d4;
    --blush-light: #fcedee;
    --brand-red: #c8323b;
    --kova-red: #a8352e;
    --coral: #ec6f6a;
    --heart-red: #d9303f;
    --heart-white: #f2f2f2;
    --ink: #111111;
    --white: #ffffff;
  }
  * { margin: 0; padding: 0; box-sizing: border-box; }
  html, body {
    width: 1200px; height: 1200px; overflow: hidden;
    background: var(--backdrop);
  }
  .poster {
    position: absolute; left: 253px; top: 111px;
    width: 694px; height: 979px; overflow: hidden;
    background: linear-gradient(180deg, var(--blush) 0%, var(--blush-light) 100%);
  }
  .red-field { position: absolute; inset: 0; width: 694px; height: 979px; }
  .heart-area { position: absolute; border-radius: 50%; }
  .heart-coral { left: -40px; top: 94px; width: 185px; height: 340px; background: var(--coral); }
  .heart-small-red { left: 100px; top: 186px; width: 106px; height: 93px; background: var(--heart-red); z-index: 3; }
  .heart-top-white { left: 190px; top: 50px; width: 102px; height: 95px; background: var(--heart-white); }
  .heart-right-white { left: 610px; top: 313px; width: 120px; height: 192px; background: var(--heart-white); }
  .heart-bottom-red { left: -40px; top: 653px; width: 185px; height: 211px; background: var(--heart-red); }
  .heart-bottom-white { left: 498px; top: 697px; width: 220px; height: 236px; background: var(--heart-white); z-index: 3; }
  .frame-line {
    position: absolute; left: 63px; top: 214px; width: 565px; height: 565px;
    border: 4px solid var(--white); z-index: 1;
  }
  .statement-card {
    position: absolute; left: 82px; top: 232px; width: 531px; height: 527px;
    background: var(--white); z-index: 2;
  }
  .lead-line {
    position: absolute; font-family: "Bebas Neue", sans-serif;
    font-size: 44px; line-height: 1; color: var(--ink); white-space: nowrap;
  }
  .lead-1 { left: 44px; top: 74px; }
  .lead-2 { left: 44px; top: 121px; }
  .lead-3 { left: 135px; top: 378px; }
  .brand-word {
    position: absolute; font-family: "Michroma", sans-serif;
    color: var(--kova-red); line-height: 1; white-space: nowrap;
  }
  .brand-name { left: 42px; top: 172px; font-size: 52px; letter-spacing: 3px; }
  .brand-close { left: 136px; top: 424px; font-size: 31px; letter-spacing: 6px; }
  .signature {
    position: absolute; left: 0; width: 694px; top: 866px;
    text-align: center; z-index: 2;
    font-family: "Bebas Neue", sans-serif; font-size: 30px; line-height: 1;
    color: var(--kova-red);
  }
</style>
</head>
<body>
  <main class="poster">
    <svg class="red-field" viewBox="0 0 694 979" aria-hidden="true">
      <polygon points="230,0 694,0 694,295" fill="var(--brand-red)"/>
    </svg>

    <div class="heart-area heart-coral" role="img" aria-label="Large coral paper heart"></div>
    <div class="heart-area heart-top-white" role="img" aria-label="Small white paper heart"></div>
    <div class="heart-area heart-right-white" role="img" aria-label="White paper heart behind frame"></div>
    <div class="heart-area heart-bottom-red" role="img" aria-label="Red paper heart"></div>

    <div class="frame-line"></div>

    <section class="statement-card">
      <p class="lead-line lead-1">There’s a reason</p>
      <p class="lead-line lead-2">we’re called</p>
      <p class="brand-word brand-name">KOVA</p>
      <p class="lead-line lead-3">is the essence of</p>
      <p class="brand-word brand-close">WHO WE ARE</p>
    </section>

    <div class="heart-area heart-small-red" role="img" aria-label="Small red paper heart"></div>
    <div class="heart-area heart-bottom-white" role="img" aria-label="Large white paper heart"></div>

    <footer class="signature">KOVA Estate Agents Group</footer>
  </main>
</body>
</html>
```